Business cards for a new business: Willow Brook Calm Healing

I would like for the card to include a lotus. The business is a healing practice so I'd like the overall colours to be pink and green and for it to have a soft feel. The name of the practice is
"Willow Brook Calm Healing", which I'd like to be included, as well as the words: "Energetic and spiritual healing to restore health, harmony and wellbeing". Also, my name - Tarik and the number: 5391 6048

Target Market(s)

Everyone interested in personal healing!

Industry/Entity Type

Business

Contact Information for Business Card

As above……..could be single or double-sided
I'd like the font for the name of the practice and my name to be in green and be a flowing, but simple font - elegant.
The background to be a light pink. See below for colours

Colors
f9d9e8
eea4c8
e567a6
d0ebe7
86cfc6
33b7a4

Requirements
Must have
• See above
Nice to have
• See above

```html
<!DOCTYPE html>
<html lang="en">
<head>
<meta charset="utf-8">
<title>Willow Brook Calm Healing – Business Cards</title>
<link rel="stylesheet" href="https://fonts.googleapis.com/css2?family=Roboto:wght@300&family=Tinos&family=Uncial+Antiqua&display=swap">
<style>
  :root {
    --canvas-bg: #ebebed;
    --card-pink: #f7dbe8;
    --card-pink-deep: #f1c9dc;
    --card-glow: #fdf1f6;
    --ink: #3c3a3d;
    --ink-soft: #4a4749;
    --ornament-dark: #3b2338;
    --ornament-mid: #5a3a55;
    --ornament-green: #9fd9c8;
  }
  * { margin: 0; padding: 0; box-sizing: border-box; }
  html, body {
    width: 1200px;
    height: 1000px;
    overflow: hidden;
    background: var(--canvas-bg);
  }
  .card-sheet {
    position: relative;
    width: 1200px;
    height: 1000px;
    display: flex;
    justify-content: center;
    align-items: center;
    gap: 40px;
  }
  .card {
    position: relative;
    width: 540px;
    height: 300px;
    overflow: hidden;
    background:
      radial-gradient(ellipse 75% 45% at 50% 48%, var(--card-glow) 0%, rgba(253,241,246,0.55) 55%, rgba(253,241,246,0) 100%),
      linear-gradient(180deg, var(--card-pink-deep) 0%, var(--card-pink) 40%, var(--card-pink) 60%, var(--card-pink-deep) 100%);
    box-shadow: 0 2px 6px rgba(0,0,0,0.12);
  }
  .card-front__ornament {
    position: absolute;
    left: 30px;
    top: 16px;
    width: 34px;
    height: 268px;
    border-radius: 50% / 12%;
    background: linear-gradient(180deg, var(--ornament-dark) 0%, var(--ornament-mid) 35%, var(--ornament-green) 50%, var(--ornament-mid) 65%, var(--ornament-dark) 100%);
  }
  .card-front__text {
    position: absolute;
    left: 80px;
    right: 20px;
    top: 0;
    text-align: center;
    color: var(--ink);
  }
  .practice-name {
    margin-top: 44px;
    font-family: "Roboto", "Helvetica Neue", Arial, sans-serif;
    font-weight: 300;
    font-size: 32px;
    letter-spacing: -0.3px;
    color: var(--ink-soft);
  }
  .practice-tagline {
    margin-top: 22px;
    font-family: "Tinos", "Times New Roman", serif;
    font-size: 16px;
    line-height: 27px;
    color: var(--ink-soft);
  }
  .practitioner-name {
    margin-top: 14px;
    font-family: "Uncial Antiqua", "Georgia", serif;
    font-size: 28px;
    line-height: 36px;
  }
  .practitioner-phone {
    font-family: "Uncial Antiqua", "Georgia", serif;
    font-size: 24px;
    letter-spacing: 1px;
    line-height: 34px;
  }
  .card-back__ornament {
    position: absolute;
    left: 22px;
    top: 110px;
    width: 496px;
    height: 90px;
    border-radius: 50%;
    background: linear-gradient(90deg, rgba(59,35,56,0) 0%, var(--ornament-dark) 18%, var(--ornament-mid) 40%, var(--ornament-green) 50%, var(--ornament-mid) 60%, var(--ornament-dark) 82%, rgba(59,35,56,0) 100%);
  }
</style>
</head>
<body>
  <main class="card-sheet">
    <section class="card card-front" aria-label="Business card front">
      <div class="card-front__ornament" role="img" aria-label="Vertical dark plum swirl ornament with a green lotus flower at its centre"></div>
      <div class="card-front__text">
        <h1 class="practice-name">Willow Brook Calm Healing</h1>
        <p class="practice-tagline">Energetic &amp; Spiritual healing to restore,<br>health, harmony and wellbeing</p>
        <p class="practitioner-name">Tarik</p>
        <p class="practitioner-phone">5391 6048</p>
      </div>
    </section>
    <section class="card card-back" aria-label="Business card back">
      <div class="card-back__ornament" role="img" aria-label="Horizontal dark plum swirl ornament with circles and a green lotus flower at its centre"></div>
    </section>
  </main>
</body>
</html>
```